Business Cards- The Estate at Brookhollow Golf Club

We would like our business cards to look more high-end. We are a wedding venue that has been in business for 60+ years. We like our logo and our colors - primarily green and a touch of gold/beige. The owner wants our business cards to look more special..

Target Market(s)

Brides who have already toured our venue

Industry/Entity Type

Wedding venue - mansion

Contact Information for Business Card

Name, email, physical address, phone number

Colors
00AB8E
00BBA5
67D7C9
C6EFE9
E9F9F6

Requirements
Must have
• I think we would like our cards to be so pretty that people will want to keep them and will remember the venue. The venue is historic (built in 1850) and beautiful.
Nice to have
• Could we put an image of the building on one side and the contact info on the other?
Should not have
• The color black

```html
<!DOCTYPE html>
<html lang="en">
<head>
<meta charset="utf-8">
<title>The Estate at Brookhollow Golf Club – Business Card</title>
<link href="https://fonts.googleapis.com/css2?family=Questrial&display=swap" rel="stylesheet">
<style>
  :root {
    --page-bg: #d9dcd6;
    --leaf: #88a142;
    --cream: #f5f1df;
    --gold: #e2d5a8;
    --logo-green: #9dbb45;
    --paper: #f7f7f5;
    --ink: #4a4a48;
    --rule: #88a142;
    --photo-top: #566072;
    --photo-bottom: #737d8c;
  }
  * { box-sizing: border-box; margin: 0; padding: 0; }
  html, body { width: 1200px; height: 1186px; overflow: hidden; }
  body {
    background: var(--page-bg);
    font-family: "Questrial", sans-serif;
    position: relative;
  }
  .card {
    position: absolute;
    left: 160px;
    width: 880px;
    height: 503px;
    border-radius: 32px;
    overflow: hidden;
  }
  .card--front { top: 62px; background: var(--leaf); }
  .card--back { top: 621px; background: var(--paper); }

  .brand {
    display: flex;
    align-items: center;
    justify-content: center;
    gap: 22px;
    line-height: 1.15;
  }
  .brand__name { text-align: center; letter-spacing: 0.06em; }
  .brand__dot {
    width: 20px; height: 20px; border-radius: 50%;
    flex: none;
  }

  .card--front .brand { position: absolute; inset: 0; }
  .card--front .brand__name { font-size: 60px; color: var(--cream); }
  .card--front .brand__dot { background: var(--gold); }

  .hero {
    position: absolute; left: 0; top: 0;
    width: 100%; height: 330px;
    background: linear-gradient(180deg, var(--photo-top), var(--photo-bottom));
  }
  .card--back .brand {
    position: absolute; left: 0; right: 0; top: 0; height: 330px;
  }
  .card--back .brand__name { font-size: 50px; color: var(--logo-green); }
  .card--back .brand__dot { background: var(--gold); }

  .contact {
    position: absolute; left: 0; right: 0; top: 330px; bottom: 0;
    display: flex; align-items: center; justify-content: center;
    gap: 36px;
  }
  .person { text-align: right; }
  .person__name { font-size: 34px; color: var(--leaf); }
  .person__role { font-size: 19px; color: var(--ink); margin-top: 6px; }
  .divider { width: 2px; height: 96px; background: var(--rule); }
  .details { list-style: none; font-size: 19px; color: var(--ink); line-height: 1.6; }
</style>
</head>
<body>
  <section class="card card--front" aria-label="Card front">
    <div class="brand">
      <span class="brand__name">The Estate at<br>Brookhollow Golf Club</span>
      <span class="brand__dot"></span>
    </div>
  </section>

  <section class="card card--back" aria-label="Card back">
    <div class="hero" role="img" aria-label="Photograph of the historic white mansion with trees under an overcast sky"></div>
    <div class="brand">
      <span class="brand__name">The Estate at<br>Brookhollow Golf Club</span>
      <span class="brand__dot"></span>
    </div>
    <div class="contact">
      <div class="person">
        <p class="person__name">Helen Whitaker</p>
        <p class="person__role">President - owner</p>
      </div>
      <span class="divider"></span>
      <ul class="details">
        <li>C : (420) 555-0148</li>
        <li>M : hwhitaker@brookhollowgolfclub.com</li>
        <li>A : 48 Orchard Lane. Millbrook, MD 21990</li>
      </ul>
    </div>
  </section>
</body>
</html>
```